Classy business card for accounting firm

We're looking for a new business card for our accounting firm. Our logo was designed by Brandloom, so all of the design info we would like to use has been provided. The specific font provided isn't required to be used.

We want the card to look classy and elegent. Probably more minimalistic, but still with some pops of color.

The options we would like to include on the card are as follows:
1. Main office phone line
2. Direct phone line
3. Email address
4. Website URL
5. Name
6. Title (CEO, President, etc.)
7. Firm Address

The design and card should be double sided!!! The drop down box in the project brief for some reason is defaulting to single sided. Not sure why this is happening.

Thanks!

Contact Information for Business Card

The options we would like to include on the card are as follows: 1. Main office phone line 2. Direct phone line 3. Email address 4. Website URL 5. Name 6. Title (CEO, President, etc.) 7. Firm Address

Requirements
Must have
• Card must be double sided.

```html
<!DOCTYPE html>
<html lang="en">
<head>
<meta charset="utf-8">
<title>Ledgerline Associates – Business Card</title>
<link rel="stylesheet" href="https://fonts.googleapis.com/css2?family=Montserrat:wght@400;500;600&display=swap">
<style>
  :root {
    --stage: #2b2b2b;
    --card-grey: #646464;
    --band-grey: #6a6a6a;
    --paper: #ffffff;
    --ink: #4a4a4a;
    --ink-soft: #6b6b6b;
    --orange: #f07a1f;
    --green: #a6bd2a;
    --rule: #bdbdbd;
  }
  * { box-sizing: border-box; margin: 0; padding: 0; }
  html, body {
    width: 1200px; height: 880px; overflow: hidden;
    background: var(--stage);
    font-family: "Montserrat", sans-serif;
  }
  .card {
    position: absolute; left: 280px;
    width: 640px; height: 366px;
    overflow: hidden;
    box-shadow: 0 8px 24px rgba(0,0,0,.35);
  }
  .card--back { top: 60px; background: var(--card-grey); }
  .card--front { top: 454px; background: var(--paper); }

  /* brand lockup */
  .brand { display: flex; flex-direction: column; align-items: flex-start; }
  .brand__name {
    display: flex; align-items: center; gap: 10px;
    font-weight: 500; font-size: 26px; letter-spacing: 1.5px;
    text-transform: uppercase; white-space: nowrap;
  }
  .brand__mark { width: 14px; height: 14px; background: var(--orange); flex: none; }
  .brand__tagline {
    display: flex; align-items: center; gap: 10px; width: 100%;
    margin-top: 6px;
    font-size: 11px; font-weight: 500; letter-spacing: 2.4px; text-transform: uppercase;
  }
  .brand__tagline::before, .brand__tagline::after {
    content: ""; flex: 1; height: 1.5px; background: var(--green);
  }
  .card--back .brand {
    position: absolute; left: 50%; top: 50%; transform: translate(-50%, -50%);
    color: #fff;
  }
  .card--back .brand__tagline { color: #eeeeee; }
  .card--front .brand { position: absolute; left: 120px; top: 138px; color: var(--ink); }
  .card--front .brand__tagline { color: var(--ink-soft); }

  /* person */
  .person { position: absolute; right: 54px; top: 38px; text-align: right; }
  .person__name { font-size: 20px; font-weight: 500; letter-spacing: 1.2px; color: var(--ink); }
  .person__title { font-size: 12px; font-weight: 500; letter-spacing: 1px; color: var(--orange); margin-top: 1px; }
  .person-tab { position: absolute; right: 0; top: 36px; width: 16px; height: 26px; background: var(--orange); }

  .divider { position: absolute; left: 320px; right: 40px; top: 222px; height: 1px; background: var(--rule); }

  .address {
    position: absolute; right: 50px; top: 232px; text-align: right;
    font-size: 12px; line-height: 1.45; color: var(--ink-soft);
  }

  .contacts {
    position: absolute; left: 120px; top: 250px; width: 210px;
    border-top: 1px solid var(--rule); padding-top: 6px;
    list-style: none; font-size: 12.5px; line-height: 1.5; color: var(--ink-soft);
  }
  .contacts li { display: flex; align-items: center; gap: 8px; }
  .contacts svg { width: 11px; height: 11px; flex: none; fill: var(--orange); }

  .footer-bands { position: absolute; left: 0; bottom: 0; width: 640px; height: 74px; }
  .website {
    position: absolute; right: 40px; bottom: 26px;
    font-size: 13px; letter-spacing: .8px; color: #fff; font-weight: 500;
  }
</style>
</head>
<body>

<section class="card card--back" aria-label="Card back">
  <div class="brand">
    <div class="brand__name"><span class="brand__mark"></span>Ledgerline Associates</div>
    <div class="brand__tagline">Solving Tax Problems</div>
  </div>
</section>

<section class="card card--front" aria-label="Card front">
  <div class="person-tab"></div>
  <div class="person">
    <div class="person__name">EVAN HARLOW</div>
    <div class="person__title">CEO/FOUNDER</div>
  </div>

  <div class="brand">
    <div class="brand__name"><span class="brand__mark"></span>Ledgerline Associates</div>
    <div class="brand__tagline">Solving Tax Problems</div>
  </div>

  <div class="divider"></div>
  <address class="address" style="font-style:normal">
    418 Alder Street, Suite 200<br>
    Fairhaven, OR 97401
  </address>

  <ul class="contacts">
    <li>
      <svg viewBox="0 0 12 12"><path d="M3 1l2 2.5-1.2 1.2a6 6 0 0 0 3.5 3.5L8.5 7 11 9l-1.5 2C5 11 1 7 1 2.5z"/></svg>
      555 210 4830
    </li>
    <li>
      <svg viewBox="0 0 12 12"><path d="M2 1h8v10H7V8H5v3H2zM3.5 2.5v1.5h1.5V2.5zm3.5 0v1.5h1.5V2.5zM3.5 5v1.5h1.5V5zm3.5 0v1.5h1.5V5z"/></svg>
      555 210 4831
    </li>
    <li>
      <svg viewBox="0 0 12 12"><path d="M1 2.5h10v7H1zm1 1v.3l4 2.7 4-2.7v-.3z"/></svg>
      evan@ledgerlinecpa.com
    </li>
  </ul>

  <svg class="footer-bands" viewBox="0 0 640 74" preserveAspectRatio="none" aria-hidden="true">
    <polygon points="0,54 440,54 440,74 0,74" fill="var(--band-grey)"/>
    <polygon points="440,22 640,0 640,74 430,74" fill="var(--orange)"/>
  </svg>
  <div class="website">WWW.LEDGERLINECPA.COM</div>
</section>

</body>
</html>
```